1940s Weekend Poster for Tourist Attraction - United Kingdom

We need a professional and stylish poster designing for our 1940s Weekend. This is the first time we have run the event and it therefore needs to be professional, eye catching and draw customers in.

The weekend is a 1940s themed event, featuring battles, vehicles, musical entertainment, so the final design should reflect this. It needs to feel nostalgic and reflect the event. We are based in the UK, so union jack, bunting etc. We have attached some example posters we like as a source of possible inspiration.

Target Market(s)

Families, re-enactors, enthusiasts.

Industry/Entity Type

Event

Font styles to use
Sans Serif
Decorative

Requirements
Must have
• The following text:
• "Marrowby Bay Narrow Tramway presents
• Dunhollow 1940's Weekend - 13th & 14th August 2016
• Come along, put your glad rags on and relive all things 1940s - with live entertainment, battle re-enactments, military vehicles and much more!
• Further details at www.dunhollowforties.co.uk or phone 01632 960418"
Nice to have
• Stylish imagery - needs to be eyecatching.
Should not have
• Clipart!

```html
<!DOCTYPE html>
<html lang="en">
<head>
<meta charset="utf-8">
<title>Dunhollow 1940's Weekend</title>
<link rel="stylesheet" href="https://fonts.googleapis.com/css2?family=Federo&family=Limelight&family=Poiret+One&display=swap">
<style>
  :root {
    --ink: #111111;
    --title-blue: #1a1fd6;
    --flag-red: #ef3566;
    --flag-red-deep: #e2285c;
    --photo-blue: #8d9ee6;
    --photo-blue-light: #b7c2f0;
    --photo-pink: #f47aa0;
    --flag-white: #ffffff;
  }
  html, body {
    margin: 0;
    padding: 0;
    width: 849px;
    height: 1200px;
    overflow: hidden;
    background: var(--flag-white);
  }
  .poster {
    position: relative;
    width: 849px;
    height: 1200px;
    overflow: hidden;
  }
  .poster__flag {
    position: absolute;
    inset: 0;
  }
  .poster__art {
    position: absolute;
    inset: 0;
  }
  .presenter {
    font-family: "Poiret One", sans-serif;
    font-size: 27px;
    fill: var(--ink);
    letter-spacing: 0.5px;
    font-weight: 700;
  }
  .title {
    font-family: "Federo", sans-serif;
    fill: var(--title-blue);
    text-anchor: middle;
  }
  .title--name { font-size: 62px; letter-spacing: 3px; }
  .title--year { font-size: 150px; letter-spacing: 2px; }
  .title--weekend { font-size: 66px; letter-spacing: 14px; }
  .dates {
    font-family: "Limelight", sans-serif;
    font-size: 25px;
    fill: var(--ink);
  }
  .invite {
    position: absolute;
    left: 38px;
    top: 628px;
    width: 620px;
    margin: 0;
    font-family: "Limelight", sans-serif;
    color: var(--ink);
    text-transform: uppercase;
    line-height: 51px;
    font-size: 19px;
  }
  .invite strong {
    font-weight: 400;
    font-size: 35px;
  }
  .footer {
    position: absolute;
    left: 36px;
    top: 1134px;
    margin: 0;
    font-family: "Poiret One", sans-serif;
    font-weight: 700;
    font-size: 16px;
    color: var(--ink);
  }
  .footer__detail { font-size: 21px; }
</style>
</head>
<body>
<main class="poster">
  <svg class="poster__flag" width="849" height="1200" viewBox="0 0 849 1200" role="img" aria-label="Union flag built from tinted 1940s photographs of fashionable women, a delivery van, a crowd at a fair and a vintage aeroplane">
    <defs>
      <linearGradient id="photoBlue" x1="0" y1="0" x2="1" y2="1">
        <stop offset="0" stop-color="var(--photo-blue-light)"/>
        <stop offset="0.5" stop-color="var(--photo-blue)"/>
        <stop offset="1" stop-color="var(--photo-blue-light)"/>
      </linearGradient>
      <linearGradient id="photoRed" x1="0" y1="0" x2="0" y2="1">
        <stop offset="0" stop-color="var(--photo-pink)"/>
        <stop offset="0.5" stop-color="var(--flag-red)"/>
        <stop offset="1" stop-color="var(--flag-red-deep)"/>
      </linearGradient>
    </defs>
    <rect class="flag-field" width="849" height="1200" fill="url(#photoBlue)"/>
    <g class="flag-saltire" stroke="var(--flag-white)" stroke-width="78">
      <line x1="-20" y1="-30" x2="869" y2="1230"/>
      <line x1="869" y1="-30" x2="-20" y2="1230"/>
    </g>
    <rect class="flag-cross-white" x="284" y="0" width="284" height="1200" fill="var(--flag-white)"/>
    <rect class="flag-cross-white" x="0" y="452" width="849" height="288" fill="var(--flag-white)"/>
    <rect class="flag-cross-red" x="336" y="0" width="176" height="1200" fill="url(#photoRed)" opacity="0.92"/>
    <rect class="flag-cross-red" x="0" y="512" width="849" height="172" fill="var(--flag-red)" opacity="0.95"/>
  </svg>

  <svg class="poster__art" width="849" height="1200" viewBox="0 0 849 1200">
    <defs>
      <path id="presenterArc" d="M 172 198 A 352 352 0 0 1 688 198"/>
      <path id="datesArc" d="M 212 452 A 428 428 0 0 0 638 452"/>
    </defs>
    <text class="presenter"><textPath href="#presenterArc" startOffset="50%" text-anchor="middle">Marrowby Bay Narrow Tramway presents</textPath></text>
    <text class="title title--name" x="424" y="236">DUNHOLLOW</text>
    <text class="title title--year" x="430" y="340">1940's</text>
    <text class="title title--weekend" x="430" y="430">WEEKEND</text>
    <text class="dates"><textPath href="#datesArc" startOffset="50%" text-anchor="middle">13TH &amp; 14TH AUGUST 2016</textPath></text>
  </svg>

  <p class="invite">
    <strong>Come along,</strong> put your glad rags on<br>
    and <strong>relive all things 1940s</strong><br>
    with <strong>live entertainment,</strong> battle<br>
    re-enactments, <strong>military vehicles</strong><br>
    <strong>and much more!</strong>
  </p>

  <p class="footer">Further details at: <span class="footer__detail">www.dunhollowforties.co.uk</span> or phone: <span class="footer__detail">01632 960418</span></p>
</main>
</body>
</html>
```